Family Owned Construction Company Needs Modern Business Cards

We need a new design for our business cards. We are a family owned construction company, Brantwell Construction, based in Mendon, Vermont and would like to add in our new logo and find a more modern look. We also want to use our old to make sure people know who we are. We do site development, highway, environmental, demolition, utility and aggregate.

Contact Information for Business Card

We want to have the office address, 418 Quarry Ridge Road, Mendon, VT 05788 and our phone (802) 555-0137 and fax (802) 555-0164 on there as well. Our website is www.brantwellinc.example. There should be a place for the person's name, title, cell number, and email address on the card. Words that we would like to be associated with our company are honesty, predictable, reliable, integrity, dedicated, built right quality, consistent, whatever it takes, and innovation. Safety is also very important to us.

Font styles to use
Serif
Sans Serif
Other font styles liked:
• Square 721 Extented

Colors
0255a3
ffffff

Requirements
Must have
• Office address, phone number and fax number. New logo with excavator
Nice to have
• That we do site development, highway, environmental, demolition, utility, and aggregate. Both logos

```html
<!DOCTYPE html>
<html lang="en">
<head>
<meta charset="utf-8">
<title>Brantwell Construction – Business Cards</title>
<link rel="stylesheet" href="https://fonts.googleapis.com/css2?family=Michroma&family=Archivo:wght@400;800&display=swap">
<style>
  :root {
    --navy: #1b3563;
    --navy-deep: #142a52;
    --white: #ffffff;
    --stage: #e9ebef;
    --burst: #c9cede;
  }
  * { margin: 0; padding: 0; box-sizing: border-box; }
  html, body { width: 1200px; height: 852px; overflow: hidden; }
  body { background: var(--stage); position: relative; font-family: "Archivo", Arial, sans-serif; }

  .card {
    position: absolute;
    width: 525px; height: 300px;
    border-radius: 18px;
    overflow: hidden;
    box-shadow: 0 10px 28px rgba(0,0,0,.22);
  }

  /* ---- Back of card: company name ---- */
  .card-back { left: 50px; top: 120px; background: var(--navy); }
  .card-back .stripe { position: absolute; left: 0; right: 0; background: var(--white); }
  .card-back .stripe-top { top: 40px; height: 14px; }
  .card-back .stripe-bottom { top: 222px; height: 30px; }
  .card-back .name-frame {
    position: absolute; left: 70px; top: 76px; width: 385px; height: 130px;
    border: 8px solid var(--white); border-radius: 14px;
    display: flex; flex-direction: column; align-items: center; justify-content: center;
    background: var(--navy);
  }
  .company-name {
    font-family: "Michroma", Arial, sans-serif;
    color: var(--white);
    font-size: 30px; letter-spacing: 1px; line-height: 1.1;
    text-transform: uppercase;
  }
  .company-sub {
    font-family: "Michroma", Arial, sans-serif;
    color: var(--white);
    font-size: 16px; letter-spacing: 2px; margin-top: 8px;
  }

  /* ---- Front of card: contact ---- */
  .card-front { left: 625px; top: 432px; background: var(--white); }
  .card-front .contact-panel {
    position: absolute; left: 0; top: 0; width: 270px; height: 240px;
    background: var(--navy);
  }
  .card-front .burst {
    position: absolute; left: 270px; top: 0; width: 255px; height: 240px;
    background: radial-gradient(circle at 40% 45%, var(--white) 0%, var(--white) 22%, var(--burst) 55%, var(--navy) 100%);
  }
  .card-front .torn-edge { position: absolute; left: 0; top: 226px; width: 525px; height: 24px; }

  .excavator-art {
    position: absolute; left: 285px; top: 30px; width: 100px; height: 170px;
    border-radius: 12px;
    background: linear-gradient(160deg, var(--navy) 0%, var(--navy-deep) 100%);
  }
  .brand-mark {
    position: absolute; left: 398px; top: 96px;
    display: flex; align-items: flex-start; gap: 5px; white-space: nowrap;
  }
  .brand-mark .square { width: 12px; height: 12px; background: var(--navy); flex: none; margin-top: 1px; }
  .brand-mark .brand-name {
    font-family: "Michroma", Arial, sans-serif;
    font-size: 8.5px; color: var(--navy); line-height: 1.45; text-transform: uppercase;
  }

  .person { position: absolute; left: 28px; top: 30px; color: var(--white); }
  .person-name { font-size: 23px; font-weight: 400; }
  .person-title { font-size: 12px; margin-top: 2px; }

  .address { position: absolute; left: 28px; top: 98px; color: var(--white); font-size: 12px; line-height: 1.35; font-style: normal; white-space: nowrap; }
  .contacts { position: absolute; left: 28px; top: 138px; list-style: none; color: var(--white); font-size: 12px; white-space: nowrap; }
  .contacts li { display: flex; align-items: center; gap: 7px; height: 17px; }
  .contacts svg { width: 11px; height: 11px; flex: none; }

  .services {
    position: absolute; left: 20px; right: 20px; top: 252px;
    color: var(--navy); font-weight: 800; font-size: 12.5px;
    text-align: center; line-height: 1.35; text-transform: uppercase; letter-spacing: .3px;
  }
</style>
</head>
<body>

  <section class="card card-back" aria-label="Business card back">
    <div class="stripe stripe-top"></div>
    <div class="stripe stripe-bottom"></div>
    <div class="name-frame">
      <div class="company-name">Brantwell</div>
      <div class="company-sub">CONSTRUCTION INC.</div>
    </div>
  </section>

  <section class="card card-front" aria-label="Business card front">
    <div class="contact-panel"></div>
    <div class="burst" role="img" aria-label="Soft light rays radiating behind the logo"></div>
    <svg class="torn-edge" viewBox="0 0 525 24" preserveAspectRatio="none" aria-hidden="true">
      <rect x="0" y="0" width="525" height="24" fill="#ffffff"/>
      <path d="M0 0 H525 V6 L505 10 L490 5 L470 12 L450 6 L430 11 L410 4 L392 10 L370 6 L350 13 L330 5 L310 11 L290 6 L270 12 L250 5 L232 11 L212 6 L190 13 L170 5 L150 11 L130 6 L110 12 L90 5 L70 11 L50 6 L30 13 L12 6 L0 10 Z" fill="#1b3563"/>
    </svg>

    <div class="excavator-art" role="img" aria-label="Excavator silhouette illustration"></div>
    <div class="brand-mark">
      <span class="square"></span>
      <span class="brand-name">Brantwell<br>Construction<br>Inc.</span>
    </div>

    <div class="person">
      <div class="person-name">Evan Marlow</div>
      <div class="person-title">Managing director</div>
    </div>

    <address class="address">
      418 Quarry Ridge Road, Mendon<br>VT 05788
    </address>

    <ul class="contacts">
      <li>
        <svg viewBox="0 0 12 12"><rect width="12" height="12" rx="2" fill="#fff"/><path d="M3 2.5 L4.8 2.5 L5.3 4.5 L4.3 5.2 Q5 6.8 6.8 7.7 L7.5 6.7 L9.5 7.2 L9.5 9 Q5 9.5 2.8 4.2 Z" fill="#1b3563"/></svg>
        (802) 555-0137
      </li>
      <li>
        <svg viewBox="0 0 12 12"><rect width="12" height="12" rx="2" fill="#fff"/><rect x="4" y="2" width="4" height="8" rx="1" fill="#1b3563"/></svg>
        (802) 555-0192
      </li>
      <li>
        <svg viewBox="0 0 12 12"><rect width="12" height="12" rx="2" fill="#fff"/><rect x="2.5" y="5" width="7" height="4.5" fill="#1b3563"/><rect x="4" y="2.5" width="4" height="2.5" fill="#1b3563"/></svg>
        (802) 555-0164
      </li>
      <li>
        <svg viewBox="0 0 12 12"><rect width="12" height="12" rx="2" fill="#fff"/><rect x="2" y="3.5" width="8" height="5" fill="none" stroke="#1b3563"/><path d="M2 3.5 L6 6.5 L10 3.5" fill="none" stroke="#1b3563"/></svg>
        evanmarlow@email.example
      </li>
    </ul>

    <p class="services">Site development, highway, environmental, demolition<br>utility and aggregate</p>
  </section>

</body>
</html>
```